Business Card Design

I am a GP with interest in Dermatology and Aesthetic Medicin, performing Botulinum Toxin Type A and Dermal Fillers treatmets in Cosmetic Dermatology clinic.

I am looking for a white colour, good quality white paper card may be of some special texture with black calligraphic writing but easy to read and not to wiggly- professional- looking.

Really appreciate your help.

Milena

Contact Information for Business Card

Cosmetic Dermatology Clinic

Dr Milena Ravitskaya, MBBS, MRCGP, DPD

Tel: 07915 462 170
milena@medpractice-mail.co.uk

```html
<!DOCTYPE html>
<html lang="en">
<head>
<meta charset="utf-8">
<title>Cosmetic Dermatology Clinic – Business Card Options</title>
<link rel="stylesheet" href="https://fonts.googleapis.com/css2?family=Arimo:wght@400;700&family=Great+Vibes&family=Oswald:wght@500&family=Tinos:wght@400;700&display=swap">
<style>
  :root {
    --mint: #4df2b0;
    --green: #2bb673;
    --green-pale: #c8f5e2;
    --grey-pale: #d9e2e0;
    --pink: #f25ab3;
    --purple: #a05cc8;
    --name-pink: #e060c8;
    --ink: #111111;
    --paper: #ffffff;
    --frame: #1a1a1a;
  }
  * { box-sizing: border-box; margin: 0; padding: 0; }
  html, body { width: 1200px; height: 750px; overflow: hidden; }
  body {
    position: relative;
    background: var(--paper);
    color: var(--ink);
    font-family: "Arimo", Arial, sans-serif;
  }

  .board-label {
    position: absolute;
    font-family: "Arimo", Arial, sans-serif;
    font-size: 30px;
    letter-spacing: 1px;
    line-height: 1;
    white-space: nowrap;
  }
  .label-option-2 { left: 104px; top: 94px; }
  .label-option-1 { left: 662px; top: 364px; }
  .label-front    { left: 1092px; top: 180px; }
  .label-back     { left: 1095px; top: 545px; }

  .card {
    position: absolute;
    background: var(--paper);
    border: 1.5px solid var(--frame);
    overflow: hidden;
  }
  .card-shapes { position: absolute; inset: 0; width: 100%; height: 100%; }

  /* Clinic name lockup: plain mark + name between rules */
  .clinic-mark {
    position: absolute;
    border-radius: 50%;
    background: var(--mint);
  }
  .rule { position: absolute; height: 4px; background: var(--green); }
  .rule-pale { position: absolute; height: 3px; background: var(--green-pale); }
  .clinic-name {
    position: absolute;
    font-family: "Oswald", "Arial Narrow", sans-serif;
    font-weight: 500;
    color: var(--ink);
    text-align: center;
    white-space: nowrap;
    letter-spacing: -0.5px;
    line-height: 1;
  }

  .doctor-name {
    position: absolute;
    font-family: "Great Vibes", cursive;
    white-space: nowrap;
    line-height: 1;
  }
  .credentials {
    position: absolute;
    font-family: "Tinos", "Times New Roman", serif;
    white-space: nowrap;
    line-height: 1;
  }
  .contact {
    position: absolute;
    font-family: "Arimo", Arial, sans-serif;
    white-space: nowrap;
    line-height: 1;
  }

  /* Option 2 — vertical card */
  .card-vertical { left: 42px; top: 144px; width: 304px; height: 525px; }
  .card-vertical .band-top    { position: absolute; left: 28px; top: 0; width: 242px; height: 27px; background: var(--pink); }
  .card-vertical .band-bottom { position: absolute; left: 28px; bottom: 0; width: 242px; height: 30px; background: var(--purple); }
  .card-vertical .clinic-mark { left: 113px; top: 60px; width: 82px; height: 82px; }
  .card-vertical .rule.upper      { left: 28px; top: 174px; width: 242px; }
  .card-vertical .clinic-name     { left: 28px; top: 189px; width: 242px; font-size: 19px; }
  .card-vertical .rule-pale.upper { left: 28px; top: 218px; width: 242px; }
  .card-vertical .doctor-name { left: 0; width: 100%; top: 286px; text-align: center; font-size: 24px; color: var(--name-pink); }
  .card-vertical .credentials { left: 0; width: 100%; top: 316px; text-align: center; font-size: 14px; color: var(--green); }
  .card-vertical .rule.lower      { left: 28px; top: 431px; width: 242px; }
  .card-vertical .contact.phone   { left: 0; width: 100%; top: 440px; text-align: center; font-size: 14px; }
  .card-vertical .contact.email   { left: 0; width: 100%; top: 460px; text-align: center; font-size: 14px; }
  .card-vertical .rule-pale.lower { left: 28px; top: 479px; width: 242px; }

  /* Option 1 — front */
  .card-front { left: 532px; top: 37px; width: 526px; height: 300px; }
  .card-front .clinic-mark     { left: 218px; top: 62px; width: 92px; height: 92px; }
  .card-front .rule.upper      { left: 144px; top: 196px; width: 240px; }
  .card-front .clinic-name     { left: 144px; top: 210px; width: 240px; font-size: 19px; }
  .card-front .rule-pale.upper { left: 144px; top: 239px; width: 240px; }

  /* Option 1 — back */
  .card-back { left: 532px; top: 408px; width: 526px; height: 297px; }
  .card-back .doctor-name { left: 22px; top: 16px; font-size: 29px; color: var(--ink); }
  .card-back .credentials { left: 22px; top: 52px; font-size: 12px; font-weight: 700; color: var(--ink); }
  .card-back .clinic-mark     { left: 364px; top: 46px; width: 68px; height: 68px; }
  .card-back .rule.upper      { left: 307px; top: 156px; width: 184px; }
  .card-back .clinic-name     { left: 307px; top: 168px; width: 184px; font-size: 14.5px; letter-spacing: -0.3px; }
  .card-back .rule-pale.upper { left: 307px; top: 190px; width: 184px; }
  .card-back .contact.phone { left: 22px; top: 240px; font-size: 15px; }
  .card-back .contact.email { left: 22px; top: 262px; font-size: 15px; }
</style>
</head>
<body>

  <p class="board-label label-option-2">Option&nbsp;&nbsp;2</p>
  <p class="board-label label-option-1">Option&nbsp;&nbsp;1</p>
  <p class="board-label label-front">Front</p>
  <p class="board-label label-back">Back</p>

  <!-- Option 2: vertical single-sided card -->
  <section class="card card-vertical" aria-label="Vertical business card">
    <div class="band-top"></div>
    <div class="clinic-mark"></div>
    <div class="rule upper"></div>
    <p class="clinic-name">COSMETIC DERMATOLOGY CLINIC</p>
    <div class="rule-pale upper"></div>
    <p class="doctor-name">Dr Milena Ravitskaya</p>
    <p class="credentials">MBBS, MRCGP, DPD</p>
    <div class="rule lower"></div>
    <p class="contact phone">Tel: 07915 462 170</p>
    <p class="contact email">milena@medpractice-mail.co.uk</p>
    <div class="rule-pale lower"></div>
    <div class="band-bottom"></div>
  </section>

  <!-- Option 1: front -->
  <section class="card card-front" aria-label="Business card front">
    <svg class="card-shapes" viewBox="0 0 526 300" preserveAspectRatio="none" aria-hidden="true">
      <rect x="200" y="20" width="326" height="20" fill="var(--grey-pale)"/>
      <path d="M0 0 H526 V20 H252 C232 20 230 40 206 40 H0 Z" fill="var(--mint)"/>
      <path d="M30 300 V274 Q30 260 44 260 H483 Q497 260 497 274 V300 Z" fill="var(--grey-pale)"/>
      <path d="M30 284 V274 Q30 260 44 260 H483 Q497 260 497 274 V284 Z" fill="var(--mint)"/>
    </svg>
    <div class="clinic-mark"></div>
    <div class="rule upper"></div>
    <p class="clinic-name">COSMETIC DERMATOLOGY CLINIC</p>
    <div class="rule-pale upper"></div>
  </section>

  <!-- Option 1: back -->
  <section class="card card-back" aria-label="Business card back">
    <svg class="card-shapes" viewBox="0 0 526 297" preserveAspectRatio="none" aria-hidden="true">
      <path d="M0 125 H288 Q303 125 303 140 V204 H495 V0 H526 V297 H0 Z" fill="var(--mint)"/>
    </svg>
    <p class="doctor-name">Dr Milena Ravitskaya</p>
    <p class="credentials">MBBS, MRCGP, DPD</p>
    <div class="clinic-mark"></div>
    <div class="rule upper"></div>
    <p class="clinic-name">COSMETIC DERMATOLOGY CLINIC</p>
    <div class="rule-pale upper"></div>
    <p class="contact phone">Tel: 07915 462 170</p>
    <p class="contact email">milena@medpractice-mail.co.uk</p>
  </section>

</body>
</html>
```